Ferrando Quispe Law Firm for Small and Medium Business: Website

We need a web design that includes coding for the Wix platform, for a new company based in Santiago, Chile, called Ferrando Quispe, Abogados y Consultores. The company is essentially a law firm, with additional advisory services in accounting, tax management and finance. The main target of the company are founders, CEOs or C-level executives of small or medium companies based in Chile.
The main menu of the web page must have the following tab options:
- Home - About us - Services – How we work -Blog – FAQ -Contact
Our main services are:

1.- Commercial and corporate law advisory
2.- Legal defense in civil, criminal, labor and family matters (litigation and arbitration)
3.- Bankruptcy and reorganization of companies
4.- Collection and recovery of assets
5.- Asset protection
6.- Financial and tax advice

We want to highlight the following services:

-Bankruptcy and reorganization of companies
-Judicial defense in civil matters
-Financial and tax advice

In addition to these services, the following will be offered:
-Lawyer at your home for special cases
-Half hour free consultation
-Monthly service packages

The final design should communicate confidence, business savvy and high execution standards and quality.

Target Market(s)

The main target of the company are founders, CEOs or C-level executives of small or medium companies based in Chile.

Industry/Entity Type

Legal industry

Coding

Coded - Design and coding required

Number of Pages Required

5+ page

Font styles to use
Serif

Requirements
Must have
• 1. Big banners para destacar los siguientes servicios: -Bankruptcy and reorganization of companies -Judicial defense in civil matters -Financial and tax advice 2. Call to action para agendar consulta legal. 3. Destacar los siguientes servicios: -Lawyer at your home for special cases -Half hour free consultation -Monthly service packages 3. Página para explicar cómo se cobra (precios transparentes): ver el siguiente sitio web: https://www.brindlemoorlegal.example/how 4. Links to Facebook, Instagram and Linkedin 5. Connection to Whatsapp.
Should not have
• Look old fashioned

```html
<!DOCTYPE html>
<html lang="en">
<head>
<meta charset="utf-8">
<title>Ferrando Quispe, Abogados y Consultores</title>
<link href="https://fonts.googleapis.com/css2?family=Exo+2:wght@500;600;700&family=Roboto:ital,wght@0,300;0,400;0,500;0,700;1,400&display=swap" rel="stylesheet">
<style>
:root{
  --green:#1a3128;
  --green-deep:#13251e;
  --gold:#b49a35;
  --gold-light:#e2d57a;
  --gold-mid:#c9b04a;
  --ink:#1f2a25;
  --text:#555;
  --line:#e6e6e6;
  --white:#fff;
}
*{margin:0;padding:0;box-sizing:border-box}
html,body{width:1200px;height:2867px;overflow:hidden}
body{position:relative;font-family:"Roboto",sans-serif;color:var(--ink);background:var(--white)}
.abs{position:absolute}
h1,h2,h3,.display{font-family:"Exo 2",sans-serif}

/* Hero */
.hero{position:absolute;left:0;top:0;width:1200px;height:610px;background:linear-gradient(90deg,#141a17 0%,#23302a 40%,#4a3a2e 70%,#6b5a44 100%)}
.hero-photo{position:absolute;left:600px;top:120px;width:420px;height:490px;background:linear-gradient(180deg,#5d6470,#3b4556 60%,#2c3444);border-radius:180px 180px 0 0;opacity:.9}
.nav{position:absolute;left:174px;top:26px;width:640px;height:92px;background:var(--green);clip-path:polygon(0 0,100% 0,98.6% 100%,0 100%)}
.brand{position:absolute;left:14px;top:32px;display:flex;align-items:center;gap:8px}
.brand-mark{width:28px;height:28px;background:var(--gold)}
.brand-name{font-family:"Exo 2",sans-serif;font-weight:500;font-size:19px;color:var(--gold-mid)}
.menu{position:absolute;left:220px;top:36px;display:flex;gap:17px;list-style:none}
.menu li{font-size:12px;font-weight:700;color:var(--white)}
.menu .active{position:relative}
.menu .active::after{content:"";position:absolute;left:-4px;right:-4px;top:40px;height:4px;background:var(--gold-light)}
.call{position:absolute;left:808px;top:26px;width:218px;height:92px;background:linear-gradient(90deg,#b39a36,#cdbb5c);clip-path:polygon(1.5% 0,100% 0,100% 100%,0 100%)}
.call svg{position:absolute;left:22px;top:30px}
.call small{position:absolute;left:58px;top:26px;font-size:9px;font-weight:500;color:var(--white);letter-spacing:.3px}
.call strong{position:absolute;left:57px;top:38px;font-size:22px;font-weight:700;color:var(--white)}
.hero h1{position:absolute;left:180px;top:218px;font-size:42px;line-height:44px;font-weight:600;color:var(--white);width:430px}
.hero .tag{position:absolute;left:178px;top:364px;font-size:21px;font-weight:300;color:var(--white)}
.btn-outline{position:absolute;left:180px;top:426px;width:181px;height:41px;border:1px solid var(--white);color:var(--white);font-size:12.5px;font-weight:700;letter-spacing:1px;display:flex;align-items:center;justify-content:center}

/* Section heads */
.sec-mark{position:absolute;width:44px;height:44px;background:linear-gradient(135deg,var(--gold),var(--gold-light))}
.sec-title{position:absolute;left:0;width:1200px;text-align:center;font-size:44px;font-weight:600;color:var(--green)}
.sec-title em{font-style:normal;color:var(--gold)}
.sec-rule{position:absolute;left:563px;width:74px;height:3px;background:var(--gold)}
.sec-lead{position:absolute;left:0;width:1200px;text-align:center;font-size:12px;line-height:19px;color:#444}

/* Services */
.services{position:absolute;left:0;top:610px;width:1200px;height:880px;background:linear-gradient(180deg,#f1f1f1,#fafafa 40%,#fff)}
.svc{position:absolute;text-align:center}
.svc .icon{width:86px;height:86px;margin:0 auto;border:3px solid var(--gold);border-radius:6px;opacity:.85}
.svc h3{font-size:18px;line-height:21px;font-weight:600;color:var(--green);margin-top:18px}
.svc p{font-size:11px;line-height:17px;color:#555;margin:12px auto 0;width:210px}
.svc .more{display:inline-flex;align-items:center;gap:6px;margin-top:18px;font-size:10.5px;font-weight:700;color:var(--gold)}
.svc.featured{background:linear-gradient(135deg,#b39a36 0%,#c6b04d 55%,#e1d57b 100%);box-shadow:0 10px 30px rgba(0,0,0,.15)}
.svc.featured .icon{border-color:var(--white)}
.svc.featured h3,.svc.featured p,.svc.featured .more{color:var(--white)}
.vline{position:absolute;width:1px;background:var(--line)}
.hline{position:absolute;height:1px;background:var(--line)}

/* Offer */
.offer-photo{position:absolute;left:175px;top:1584px;width:448px;height:449px;background:linear-gradient(135deg,#6a6156,#3a3631 55%,#8a7d6b)}
.offer h2{position:absolute;left:648px;top:1590px;font-size:36px;line-height:41px;font-weight:600;color:var(--green)}
.offer h2 em{font-style:normal;color:var(--gold)}
.perk{position:absolute;left:538px;width:485px;height:84px;background:var(--white);border:1px solid var(--line)}
.perk .sq{position:absolute;top:-1px;width:86px;height:84px;background:var(--gold)}
.perk p{position:absolute;top:50%;transform:translateY(-50%);font-size:15px;line-height:22px;color:#222}

/* Cases */
.cases{position:absolute;left:0;top:2092px;width:1200px;height:543px;background:linear-gradient(180deg,#fff 0%,#f4f4f4 60%,#e9e9e9)}
.case{position:absolute;top:2379px;width:273px;height:184px;background:var(--white);border-radius:8px;box-shadow:0 4px 18px rgba(0,0,0,.06)}
.case .avatar{position:absolute;left:11px;top:-30px;width:60px;height:60px;border-radius:50%;background:linear-gradient(135deg,#8a6d5a,#3d2f28)}
.case .quote{position:absolute;right:14px;top:-12px;font-family:"Exo 2",sans-serif;font-size:52px;line-height:52px;font-weight:700;color:#d6d6d6}
.case blockquote{position:absolute;left:11px;top:48px;width:250px;font-size:10.5px;line-height:16px;font-style:italic;color:#555}
.case .rule{position:absolute;left:11px;right:11px;top:120px;height:1px;background:var(--line)}
.case .who{position:absolute;left:11px;top:134px;font-size:12px;font-weight:500;color:var(--gold)}
.case .role{position:absolute;left:11px;top:152px;font-size:9px;color:#333}
.arrow-btn{position:absolute;top:2441px;width:46px;height:46px;border-radius:50%;background:var(--white);box-shadow:0 2px 8px rgba(0,0,0,.1);display:flex;align-items:center;justify-content:center}

/* Footer */
.footer{position:absolute;left:0;top:2635px;width:1200px;height:232px;background:var(--green)}
.f-logo{position:absolute;left:174px;top:35px;width:117px;height:117px;background:linear-gradient(135deg,#b39a36,#e1d57b);display:flex;align-items:center;justify-content:center;text-align:center;font-family:"Exo 2",sans-serif;font-weight:600;font-size:15px;line-height:18px;color:var(--green)}
.f-col{position:absolute;top:36px;color:var(--white)}
.f-col h4{font-family:"Exo 2",sans-serif;font-size:14px;font-weight:700;margin-bottom:16px}
.f-col p,.f-col li{font-size:10px;line-height:14px}
.f-col ul{list-style:none}
.f-col li{margin-bottom:5.5px}
.social{display:flex;gap:5px}
.social span{width:26px;height:26px;border-radius:50%;background:var(--white)}
.f-rule{position:absolute;left:174px;top:183px;width:852px;height:1px;background:var(--gold)}
.f-legal{position:absolute;top:208px;font-size:10px;color:var(--white)}
</style>
</head>
<body>

<header class="hero">
  <div class="hero-photo" role="img" aria-label="Lawyer in a suit with arms crossed, scales of justice and model houses behind"></div>
  <nav class="nav">
    <div class="brand"><span class="brand-mark"></span><span class="brand-name">Ferrando Quispe</span></div>
    <ul class="menu">
      <li class="active">Home</li><li>About us</li><li>Services</li><li>How we work</li><li>Blog</li><li>FAQ</li><li>Contact</li>
    </ul>
  </nav>
  <div class="call">
    <svg width="30" height="30" viewBox="0 0 24 24" fill="none" stroke="#fff" stroke-width="1.5"><path d="M5 3h3l2 5-2 1.5a11 11 0 0 0 6.5 6.5L16 14l5 2v3a2 2 0 0 1-2 2A16 16 0 0 1 3 5a2 2 0 0 1 2-2z"/></svg>
    <small>FREE CONSULTATION</small>
    <strong>(123) 555-0147</strong>
  </div>
  <h1>You know like no other how it feels to be on the edge...</h1>
  <p class="tag">Fighting for Our Clients 24/7</p>
  <a class="btn-outline">FREE CONSULTATION</a>
</header>

<section class="services">
  <div class="sec-mark" style="left:578px;top:74px"></div>
  <h2 class="sec-title" style="top:128px"><em>Our</em> Services</h2>
  <div class="sec-rule" style="top:189px"></div>
  <p class="sec-lead" style="top:205px">Lorem ipsum dolor sit amet, consectetur adipiscing elit, sed do eiusmod<br>tempor incididunt ut labore et dolore magna aliqua</p>
</section>

<div class="svc" style="left:174px;top:896px;width:246px;padding-top:16px">
  <div class="icon" role="img" aria-label="Handshake over a contract icon"></div>
  <h3>Commercial and<br>corporate law advisory</h3>
  <p>Lorem ipsum dolor sit amet, consect adipiscing elit, sed do eiusmod tempor incididunt ut labore</p>
  <span class="more">READ MORE <svg width="14" height="8" viewBox="0 0 14 8" fill="none" stroke="currentColor" stroke-width="1.5"><path d="M0 4h12M9 1l3 3-3 3"/></svg></span>
</div>
<div class="svc featured" style="left:420px;top:896px;width:327px;height:289px;padding-top:16px">
  <div class="icon" role="img" aria-label="Handcuffs and gavel icon"></div>
  <h3>Legal defense in civil, criminal,<br>labor and family matters</h3>
  <p>Lorem ipsum dolor sit amet, consect adipiscing elit, sed do eiusmod tempor incididunt ut labore</p>
  <span class="more">READ MORE <svg width="14" height="8" viewBox="0 0 14 8" fill="none" stroke="currentColor" stroke-width="1.5"><path d="M0 4h12M9 1l3 3-3 3"/></svg></span>
</div>
<div class="svc" style="left:747px;top:896px;width:279px;padding-top:16px">
  <div class="icon" role="img" aria-label="House with padlock icon"></div>
  <h3>Bankruptcy and reorganization<br>of companies</h3>
  <p>Lorem ipsum dolor sit amet, consect adipiscing elit, sed do eiusmod tempor incididunt ut labore</p>
  <span class="more">READ MORE <svg width="14" height="8" viewBox="0 0 14 8" fill="none" stroke="currentColor" stroke-width="1.5"><path d="M0 4h12M9 1l3 3-3 3"/></svg></span>
</div>

<div class="hline" style="left:174px;top:1185px;width:852px"></div>
<div class="vline" style="left:420px;top:1185px;height:284px"></div>
<div class="vline" style="left:747px;top:1185px;height:284px"></div>

<div class="svc" style="left:174px;top:1185px;width:246px;padding-top:34px">
  <div class="icon" role="img" aria-label="Banknotes and coin stack icon"></div>
  <h3>Collection and recovery<br>of assets</h3>
  <p>Lorem ipsum dolor sit amet, consect adipiscing elit, sed do eiusmod tempor incididunt ut labore</p>
  <span class="more">READ MORE <svg width="14" height="8" viewBox="0 0 14 8" fill="none" stroke="currentColor" stroke-width="1.5"><path d="M0 4h12M9 1l3 3-3 3"/></svg></span>
</div>
<div class="svc" style="left:420px;top:1185px;width:327px;padding-top:34px">
  <div class="icon" role="img" aria-label="Umbrella sheltering a house icon"></div>
  <h3>Asset protection</h3>
  <p>Lorem ipsum dolor sit amet, consect adipiscing elit, sed do eiusmod tempor incididunt ut labore</p>
  <span class="more" style="margin-top:39px">READ MORE <svg width="14" height="8" viewBox="0 0 14 8" fill="none" stroke="currentColor" stroke-width="1.5"><path d="M0 4h12M9 1l3 3-3 3"/></svg></span>
</div>
<div class="svc" style="left:747px;top:1185px;width:279px;padding-top:34px">
  <div class="icon" role="img" aria-label="Tax document with dollar sign icon"></div>
  <h3>Financial and tax<br>advice</h3>
  <p>Lorem ipsum dolor sit amet, consect adipiscing elit, sed do eiusmod tempor incididunt ut labore</p>
  <span class="more">READ MORE <svg width="14" height="8" viewBox="0 0 14 8" fill="none" stroke="currentColor" stroke-width="1.5"><path d="M0 4h12M9 1l3 3-3 3"/></svg></span>
</div>

<section class="offer">
  <div class="offer-photo" role="img" aria-label="Two lawyers in suits seated in a courtroom"></div>
  <h2><em>Ferrando Quispe,</em> Abogados<br>y Consultores offer you</h2>
  <div class="perk" style="top:1700px"><span class="sq" style="left:-1px"></span><p style="left:104px">Lawyers of excellence in litigation and professionals in<br>finance and the tax area with vast experience</p></div>
  <div class="perk" style="top:1802px"><span class="sq" style="right:-1px"></span><p style="left:27px">Executive approach to solve your problem with a<br>sense of urgency</p></div>
  <div class="perk" style="top:1906px"><span class="sq" style="left:-1px"></span><p style="left:103px">Payment facilities and multi payment options</p></div>
</section>

<section class="cases">
  <div class="sec-mark" style="left:578px;top:56px"></div>
  <h2 class="sec-title" style="top:110px"><em>Case</em> Studies</h2>
  <div class="sec-rule" style="top:170px"></div>
  <p class="sec-lead" style="top:195px">Lorem ipsum dolor sit amet, consectetur adipiscing elit, sed do eiusmod<br>tempor incididunt ut labore et dolore magna aliqua</p>
</section>

<div class="arrow-btn" style="left:96px"><svg width="10" height="14" viewBox="0 0 10 14" fill="none" stroke="#1a3128" stroke-width="2"><path d="M8 1 2 7l6 6"/></svg></div>
<div class="arrow-btn" style="left:1043px"><svg width="10" height="14" viewBox="0 0 10 14" fill="none" stroke="#1a3128" stroke-width="2"><path d="m2 1 6 6-6 6"/></svg></div>

<article class="case" style="left:174px">
  <div class="avatar" role="img" aria-label="Client portrait"></div><span class="quote">&rdquo;</span>
  <blockquote>Somewhere right now, there is a first time CEO out there, not working with BrightPath, not following their 100-Day Action Plan, and I am worried for them.</blockquote>
  <div class="rule"></div><p class="who">Lena Varga</p><p class="role">CEO Norvale Partners Group</p>
</article>
<article class="case" style="left:463px">
  <div class="avatar" role="img" aria-label="Client portrait"></div><span class="quote">&rdquo;</span>
  <blockquote>Lorem ipsum dolor sit amet, consectetur adipi-scing elit, sed do eiusmod tempor to incididunt ut labore et dolore magna for aliqua. Quis ipsum suspendisse.</blockquote>
  <div class="rule"></div><p class="who">Lena Varga</p><p class="role">CEO Norvale Partners Group</p>
</article>
<article class="case" style="left:753px">
  <div class="avatar" role="img" aria-label="Client portrait"></div><span class="quote">&rdquo;</span>
  <blockquote>Lorem ipsum dolor sit amet, consectetur adipi-scing elit, sed do eiusmod tempor to incididunt ut labore et dolore magna for aliqua. Quis ipsum suspendisse.</blockquote>
  <div class="rule"></div><p class="who">Lena Varga</p><p class="role">CEO Norvale Partners Group</p>
</article>

<footer class="footer">
  <div class="f-logo">Ferrando<br>Quispe</div>
  <div class="f-col" style="left:363px">
    <h4>Our Address</h4>
    <p>218 Calle Norte Alta<br>Santiago, Chile</p>
    <p style="margin-top:14px">Phone: 22558103<br>Email: hello@ferrandoquispe.example<br>Office Time: 10AM- 5PM</p>
  </div>
  <div class="f-col" style="left:575px">
    <h4>Quick Links</h4>
    <ul><li>Home</li><li>About</li><li>Practice Areas</li><li>Contact</li><li>Site Map</li></ul>
  </div>
  <div class="f-col" style="left:715px;top:66px">
    <ul><li>Privacy Policy</li><li>Testimonials</li><li>News</li><li>FAQ</li></ul>
  </div>
  <div class="f-col" style="left:867px">
    <h4>Follow Us</h4>
    <div class="social"><span></span><span></span><span></span></div>
  </div>
  <div class="f-rule"></div>
  <p class="f-legal" style="left:174px">© Ferrando Quispe 2021. All Rights Reserved.</p>
  <p class="f-legal" style="left:879px">Terms of Use &nbsp;| &nbsp;Privacy Policy</p>
</footer>

</body>
</html>
```